Lena Marwick Biz Card
biz card and stationary
Lena Marwick Biz Card - Financial Services
Creative Brief
Bright & Fun-filled
Lena Marwick
Independent Agent
Charlotte, NC
Lenamarwick@quillpost.example
www.marwickInsurance.example
Please use the head shot attached and the logo.
I will be uploading an example of content for the back of their card. please use that information.

```html
<!DOCTYPE html>
<html lang="en">
<head>
<meta charset="utf-8">
<title>Lena Marwick Business Card</title>
<link rel="stylesheet" href="https://fonts.googleapis.com/css2?family=Tinos:wght@400;700&display=swap">
<style>
  :root {
    --frame: #4d4d4d;
    --sheet: #c9c9c9;
    --white: #ffffff;
    --ink: #111111;
    --navy: #0b2a7a;
    --navy-deep: #061a4f;
    --blue: #1a4fa3;
    --green: #5bb531;
    --green-light: #8fd14f;
    --green-deep: #3f9a2a;
    --grey-text: #444444;
  }
  * { box-sizing: border-box; margin: 0; padding: 0; }
  html, body { width: 1200px; height: 713px; overflow: hidden; }
  body {
    background: var(--frame);
    font-family: "Tinos", "Times New Roman", serif;
    color: var(--ink);
    position: relative;
  }
  .sheet {
    position: absolute; left: 14px; top: 14px; width: 1172px; height: 685px;
    background: var(--sheet);
  }
  .card {
    position: absolute; width: 550px; height: 312px;
    border-radius: 14px; overflow: hidden;
    box-shadow: 0 1px 3px rgba(0,0,0,.25);
  }
  .card--front { left: 29px; top: 29px; background: var(--white); }
  .card--back-navy { left: 606px; top: 29px;
    background: radial-gradient(ellipse at 60% 40%, #1d4fb8 0%, var(--navy) 45%, var(--navy-deep) 100%); }
  .card--back-white { left: 29px; top: 366px; height: 306px; background: var(--white); }
  .card--back-green { left: 606px; top: 366px; height: 306px;
    background: radial-gradient(ellipse at 75% 45%, var(--green-light) 0%, var(--green) 50%, var(--green-deep) 100%); }

  /* front */
  .brand { position: absolute; left: 30px; top: 38px; display: flex; align-items: center; gap: 10px; }
  .brand__dot { width: 30px; height: 30px; border-radius: 50%; background: var(--blue); }
  .brand__name { font-size: 30px; color: var(--blue); font-weight: 400; line-height: 1; }
  .headshot { position: absolute; left: 448px; top: 34px; width: 88px; height: 112px;
    background: linear-gradient(180deg, #d9b98f 0%, #b08060 55%, #3a3a3a 100%);
    border: 2px solid #ddd; }
  .agent { position: absolute; left: 30px; top: 180px; }
  .agent__name { font-size: 25px; font-weight: 700; color: var(--blue); line-height: 1.1; }
  .agent__title { font-size: 13px; color: var(--grey-text); margin-top: 2px; }
  .swoosh { position: absolute; left: 0; top: 0; width: 550px; height: 312px; }
  .contact { position: absolute; right: 18px; top: 234px; text-align: right;
    font-size: 12px; line-height: 1.4; color: var(--grey-text); font-style: normal; }

  /* backs */
  .offer-title { font-size: 19px; font-weight: 700; }
  .offer-list { list-style: none; font-size: 18px; line-height: 1.18; }
  .card--back-navy .mark-name { position: absolute; left: 0; right: 0; top: 40px; text-align: center;
    color: var(--white); font-size: 28px; }
  .card--back-navy .offers { position: absolute; left: 0; right: 0; top: 150px; text-align: center; color: var(--white); }
  .card--back-navy .offer-title { margin-bottom: 6px; }
  .card--back-white .offers { position: absolute; left: 24px; top: 34px; }
  .card--back-white .offer-title { color: var(--blue); font-size: 21px; margin-bottom: 30px; }
  .card--back-white .mark-name { position: absolute; right: 30px; top: 130px; color: var(--blue); font-size: 28px; }
  .card--back-green .offers { position: absolute; left: 24px; top: 40px; color: var(--white); }
  .card--back-green .offer-title { margin-bottom: 22px; }
  .card--back-green .mark-name { position: absolute; right: 30px; top: 125px; color: var(--white); font-size: 28px; }
</style>
</head>
<body>
<main class="sheet">
  <section class="card card--front">
    <svg class="swoosh" viewBox="0 0 550 312" aria-hidden="true">
      <path d="M0 236 C110 262 220 276 330 312 L0 312 Z" fill="#1a4fa3"/>
      <path d="M0 262 C100 282 190 294 260 312 L0 312 Z" fill="#0b2a7a"/>
      <path d="M0 226 C120 252 240 270 346 312 L330 312 C220 276 110 262 0 236 Z" fill="#5bb531"/>
    </svg>
    <div class="brand"><span class="brand__dot"></span><span class="brand__name">Marwick Insurance</span></div>
    <div class="headshot" role="img" aria-label="Head shot of the agent"></div>
    <div class="agent">
      <p class="agent__name">Lena Marwick</p>
      <p class="agent__title">Independent Agent</p>
    </div>
    <address class="contact">
      Charlotte, NC<br>
      Phone: 704-555-0187<br>
      Email: Lenamarwick@quillpost.example<br>
      www.marwickInsurance.example
    </address>
  </section>

  <section class="card card--back-navy">
    <p class="mark-name">Marwick Insurance</p>
    <div class="offers">
      <p class="offer-title">I can also help you with.......</p>
      <ul class="offer-list">
        <li>Long-Term Care Insurance | Fixed Annuities</li>
        <li>Life Insurance | Medicare Supplement Insurance</li>
        <li>Individual Major Medical Insurance | Final Expense Insurance</li>
        <li>Medicare Advantage Plans</li>
      </ul>
    </div>
  </section>

  <section class="card card--back-white">
    <div class="offers">
      <p class="offer-title">I can also help you with.......</p>
      <ul class="offer-list">
        <li>Long-Term Care Insurance</li>
        <li>Fixed Annuities</li>
        <li>Life Insurance</li>
        <li>Medicare Supplement Insurance</li>
        <li>&nbsp;Individual Major Medical Insurance</li>
        <li>Final Expense Insurance</li>
        <li>Medicare Advantage Plans</li>
      </ul>
    </div>
    <p class="mark-name">Marwick Insurance</p>
  </section>

  <section class="card card--back-green">
    <div class="offers">
      <p class="offer-title">I can also help you with.......</p>
      <ul class="offer-list">
        <li>Long-Term Care Insurance</li>
        <li>Fixed Annuities</li>
        <li>Life Insurance</li>
        <li>Medicare Supplement Insurance</li>
        <li>&nbsp;Individual Major Medical Insurance</li>
        <li>Final Expense Insurance</li>
        <li>Medicare Advantage Plans</li>
      </ul>
    </div>
    <p class="mark-name">Marwick Insurance</p>
  </section>
</main>
</body>
</html>
```